marcel's mobile mechanic

a business card that will get attention from clients
- name of the business: M'S MOBILE MECHANIC
- we currently do not have a logo and do not need one at the moment, happy for the designers to just put the business name on the card using appropriate fonts

Target Market(s)

low cost mobile repairs

Industry/Entity Type

Business

Contact Information for Business Card

attracts customers

Font styles to use
Sans Serif

Colors
0255a3
fbee3d
000000

Requirements
Must have
• (555) 318-4907
• Marcel Treviño
• for lower income target market
Nice to have
• "we save you money"
• Easy to read
Should not have
• nothing comes to mind

```html
<!DOCTYPE html>
<html lang="en">
<head>
<meta charset="utf-8">
<title>M'S Mobile Mechanic – Business Card</title>
<link rel="stylesheet" href="https://fonts.googleapis.com/css2?family=Roboto:wght@400;500&display=swap">
<style>
  :root {
    --navy: #0b2d5b;
    --orange: #f7921e;
    --paper: #f1f1f1;
    --white: #ffffff;
    --backdrop: #6e4d36;
  }
  * { margin: 0; padding: 0; box-sizing: border-box; }
  html, body { width: 1200px; height: 960px; overflow: hidden; }
  body {
    position: relative;
    background: var(--backdrop);
    font-family: "Roboto", Arial, sans-serif;
  }
  .card {
    position: absolute;
    width: 600px;
    height: 342px;
    overflow: hidden;
    box-shadow: 0 3px 6px rgba(0,0,0,0.35);
  }
  .card--front { left: 314px; top: 113px; background: var(--paper); }
  .card--back { left: 311px; top: 472px; background: var(--orange); }

  .business-name {
    position: absolute;
    left: 0; right: 0;
    text-align: center;
    font-family: "Roboto", Arial, sans-serif;
    font-weight: 500;
    color: var(--navy);
    text-transform: uppercase;
    white-space: nowrap;
    letter-spacing: 1px;
  }
  .card--front .business-name { top: 78px; font-size: 34px; line-height: 40px; }
  .card--back .business-name { top: 130px; font-size: 44px; line-height: 52px; }

  .divider { position: absolute; left: 0; top: 200px; width: 600px; height: 14px; }

  .contact-band {
    position: absolute;
    left: 0; top: 212px;
    width: 600px; height: 130px;
    background: var(--navy);
    color: var(--white);
    text-align: center;
  }
  .contact-band__name {
    margin-top: 20px;
    font-size: 20px;
    font-weight: 500;
    color: var(--orange);
    text-transform: uppercase;
    letter-spacing: 0.2px;
  }
  .contact-band__role { font-size: 15px; font-weight: 500; margin-top: 1px; }
  .contact-band__address { font-size: 14px; margin-top: 9px; }
  .contact-band__lines {
    display: flex;
    justify-content: center;
    align-items: center;
    gap: 6px;
    font-size: 14px;
    margin-top: 5px;
  }
  .contact-band__item { display: inline-flex; align-items: center; gap: 4px; }
  .contact-band__item svg { width: 12px; height: 12px; fill: var(--orange); }

  .tagline {
    position: absolute;
    left: 0; right: 0; top: 290px;
    display: flex;
    justify-content: center;
    align-items: center;
    color: var(--white);
    font-size: 14px;
  }
  .tagline__rule {
    width: 60px; height: 2px;
    background: linear-gradient(90deg, rgba(11,45,91,0), var(--navy));
  }
  .tagline__rule--right { background: linear-gradient(90deg, var(--navy), rgba(11,45,91,0)); }
</style>
</head>
<body>

  <section class="card card--front">
    <p class="business-name">M'S Mobile Mechanic</p>

    <svg class="divider" viewBox="0 0 600 14" aria-hidden="true">
      <rect x="4" y="5" width="590" height="4" fill="var(--orange)"/>
      <circle cx="5" cy="7" r="4" fill="var(--paper)" stroke="var(--orange)" stroke-width="2"/>
      <circle cx="593" cy="7" r="5" fill="var(--paper)" stroke="var(--orange)" stroke-width="3"/>
    </svg>

    <div class="contact-band">
      <p class="contact-band__name">Marcel Treviño</p>
      <p class="contact-band__role">CEO/FOUNDER</p>
      <p class="contact-band__address">412 Cedarbrook Road, Fairview, Alaska 99501</p>
      <div class="contact-band__lines">
        <span class="contact-band__item">
          <svg viewBox="0 0 24 24"><path d="M6.6 10.8a15 15 0 0 0 6.6 6.6l2.2-2.2c.3-.3.7-.4 1-.2 1.1.4 2.3.6 3.6.6.6 0 1 .4 1 1V20c0 .6-.4 1-1 1A17 17 0 0 1 3 4c0-.6.4-1 1-1h3.5c.6 0 1 .4 1 1 0 1.3.2 2.5.6 3.6.1.3 0 .7-.2 1z"/></svg>
          (555) 318-4907
        </span>
        <span class="contact-band__item">
          <svg viewBox="0 0 24 24"><path d="M2 5h20v14H2z"/><path d="M2 5l10 8 10-8" fill="none" stroke="var(--navy)" stroke-width="2"/></svg>
          info@msmech.com
        </span>
        <span class="contact-band__item">
          <svg viewBox="0 0 24 24"><circle cx="12" cy="12" r="10"/></svg>
          www.msmech.com
        </span>
      </div>
    </div>
  </section>

  <section class="card card--back">
    <p class="business-name">M'S Mobile Mechanic</p>
    <p class="tagline">
      <span class="tagline__rule"></span>
      <span>For lower income target market</span>
      <span class="tagline__rule tagline__rule--right"></span>
    </p>
  </section>

</body>
</html>
```